A start up Private Wine Label for export to Asia.

We are looking for the best graphic design for our very first wine label Corvessa Cellars and would like the following requirements:

1. Black background - explore and play around the shade of black
2. Gold Shimmery Colour Font
3. Font should be a cursive classic posh that says Corvessa Cellars
4. We would like the front graphic design to be simple and elegant and has a traditional classic feel to it.

Target Market(s)

Small scale to test the upper class market for export to Asia

Font styles to use
Script

Colors

Designer to choose colors to be used in the design.

Requirements
Must have
• Gold font for the label Corvessa Cellars with shimmery touch to it.
• Elegant black background.
• Simple but elegant design.
• Attractive to the upper class market in Asia.
Nice to have
• Explore and play around with your imagination.

```html
<!DOCTYPE html>
<html lang="en">
<head>
<meta charset="utf-8">
<title>Corvessa Cellars – Wine Label</title>
<link href="https://fonts.googleapis.com/css2?family=Parisienne&family=Roboto+Condensed:wght@400;700&family=Montserrat:wght@400;500&display=swap" rel="stylesheet">
<style>
  :root {
    --label-black: #000000;
    --tab-grey: #2b2b2b;
    --gold-deep: #6e5316;
    --gold-mid: #c9a54a;
    --gold-light: #f6e4a6;
    --gold-pale: #fff3c8;
    --text-white: #ffffff;
    --text-muted: #5a5a5a;
  }
  * { margin: 0; padding: 0; box-sizing: border-box; }
  html, body { width: 1200px; height: 800px; overflow: hidden; background: var(--label-black); }
  .label {
    position: relative; width: 1200px; height: 800px;
    background: var(--label-black); color: var(--text-white);
    font-family: "Roboto Condensed", sans-serif;
  }
  .ornament-band {
    position: absolute; left: 0; width: 1200px;
    background: linear-gradient(90deg, #1a1204 0%, var(--gold-deep) 12%, #2a1f08 25%, var(--gold-mid) 38%, #2a1f08 50%, var(--gold-mid) 62%, #2a1f08 75%, var(--gold-deep) 88%, #1a1204 100%);
    opacity: 0.85;
  }
  .ornament-band--top { top: 52px; height: 136px; }
  .ornament-band--bottom { top: 578px; height: 142px; }
  .gold-rule {
    position: absolute; left: 0; width: 1200px;
    background: linear-gradient(90deg, var(--gold-deep), var(--gold-light) 30%, var(--gold-mid) 60%, var(--gold-light) 85%, var(--gold-deep));
  }
  .gold-rule--top-a { top: 184px; height: 5px; }
  .gold-rule--top-b { top: 194px; height: 8px; }
  .gold-rule--bottom-a { top: 552px; height: 8px; }
  .gold-rule--bottom-b { top: 568px; height: 5px; }
  .main-panel {
    position: absolute; left: 0; top: 202px; width: 1200px; height: 350px;
    background: var(--label-black);
  }
  .brand-tab {
    position: absolute; left: 417px; top: 0; width: 366px; height: 146px;
    background: var(--tab-grey); border-radius: 0 0 70px 70px;
    text-align: center; padding-top: 30px;
  }
  .brand-tab__name {
    font-weight: 700; font-size: 29px; line-height: 1.05; letter-spacing: 1px;
  }
  .brand-tab__sub {
    font-family: "Montserrat", sans-serif; font-size: 15px; letter-spacing: 3px; margin-top: 12px;
  }
  .wordmark {
    position: absolute; left: 0; top: 222px; width: 1200px; text-align: center;
    font-family: "Parisienne", cursive; font-size: 116px; line-height: 128px;
    background: linear-gradient(180deg, var(--gold-pale) 0%, var(--gold-light) 35%, var(--gold-mid) 60%, var(--gold-light) 85%, var(--gold-deep) 100%);
    -webkit-background-clip: text; background-clip: text; color: transparent;
  }
  .wordmark__line { display: block; }
  .varietal {
    position: absolute; left: 0; top: 505px; width: 1200px; text-align: center;
    font-family: "Montserrat", sans-serif; font-size: 18px; letter-spacing: 3px;
  }
  .about {
    position: absolute; left: 46px; top: 236px; width: 160px;
    font-size: 9.5px; line-height: 13px; text-transform: uppercase; letter-spacing: 0.4px;
  }
  .about p + p { margin-top: 10px; }
  .origin {
    position: absolute; left: 46px; top: 408px;
    font-weight: 700; font-size: 23px; line-height: 25px; letter-spacing: 1px; text-transform: uppercase;
  }
  .footnote {
    position: absolute; left: 46px; top: 562px; width: 140px;
    font-size: 10px; line-height: 14px; color: var(--text-muted);
  }
  .dates {
    position: absolute; right: 17px; top: 228px; text-align: right;
    text-transform: uppercase;
  }
  .dates__label { font-family: "Montserrat", sans-serif; font-size: 17px; letter-spacing: 2px; }
  .dates__value { font-family: "Montserrat", sans-serif; font-size: 31px; letter-spacing: 1px; margin-top: 6px; margin-bottom: 22px; }
  .dates__note { font-weight: 700; font-size: 31px; line-height: 35px; letter-spacing: 1.5px; margin-top: -4px; }
  .volume {
    position: absolute; left: 0; top: 766px; width: 1200px; text-align: center;
    font-family: "Montserrat", sans-serif; font-size: 15px; letter-spacing: 2px;
  }
</style>
</head>
<body>
  <main class="label">
    <div class="ornament-band ornament-band--top" role="img" aria-label="Gold damask ornament border"></div>
    <div class="ornament-band ornament-band--bottom" role="img" aria-label="Gold damask ornament border"></div>
    <div class="main-panel"></div>
    <div class="gold-rule gold-rule--top-a"></div>
    <div class="gold-rule gold-rule--top-b"></div>
    <div class="gold-rule gold-rule--bottom-a"></div>
    <div class="gold-rule gold-rule--bottom-b"></div>

    <header class="brand-tab">
      <div class="brand-tab__name">CORVESSA<br>CELLARS</div>
      <div class="brand-tab__sub">BREWING COMPANY</div>
    </header>

    <h1 class="wordmark">
      <span class="wordmark__line">Corvessa</span>
      <span class="wordmark__line">Cellars</span>
    </h1>
    <div class="varietal">CLASSIC WINE</div>

    <section class="about">
      <p>A microbrewery or craft brewery is a brewery that</p>
      <p>produces small amounts of beer, typically much smaller than large-scale corporate breweries, and is independently owned.</p>
    </section>
    <div class="origin">Locally<br>brewed in<br>Portland,<br>Oregon.</div>
    <div class="footnote">Such beverages are made with care.</div>

    <section class="dates">
      <div class="dates__label">Bottled on</div>
      <div class="dates__value">12/01/19</div>
      <div class="dates__label">Best before</div>
      <div class="dates__value">08/01/20</div>
      <div class="dates__note">Please<br>drink<br>fresh</div>
    </section>

    <div class="volume">500 ML • 7.5% ALC.</div>
  </main>
</body>
</html>
```